Webdesign Tischlerei Wendholt GmbH
Zielgruppe
Tischlerei - Meisterbetrieb -> Zielgruppe Privatkunden + gewerbliche Kunden
Aufgabenstellung
KEINE Kopie der alten Seite, da sich das gesamte Erscheinungsbild wesentlich moderner gestaltet... aufbauend auf dem neuen Unternehmenslogo. Es soll mit den vorhandenen Farben aus dem Logo gearbeitet werden - jedoch nicht verspielt sein.
ACHTUNG: bei den beiden mitgelieferten Dateien, welche dir Icons als Abbildung haben, ist nicht korrekte Logo verbaut, sofern diese Icons nicht verwendbar sind, bitte passende Logos für die einzelnen Kategoerien Wählen.

```html
<!DOCTYPE html>
<html lang="de">
<head>
<meta charset="utf-8">
<title>Tischlerei Wendholt GmbH</title>
<link href="https://fonts.googleapis.com/css2?family=Noto+Serif:wght@400;700&family=Nunito+Sans:wght@400;600;700&display=swap" rel="stylesheet">
<style>
:root{
  --bg:#eceef0;
  --dark:#14262a;
  --wood:#b87430;
  --wood-light:#c8893f;
  --white:#ffffff;
  --ink:#1d2a2c;
}
*{box-sizing:border-box;margin:0;padding:0}
html,body{width:1200px;height:2400px;overflow:hidden;background:var(--bg)}
body{font-family:"Nunito Sans",Arial,sans-serif;color:var(--ink)}
.page{position:absolute;left:168px;top:80px;width:928px;height:2404px;background:var(--white);transform:scale(0.9317);transform-origin:0 0;overflow:hidden}
.abs{position:absolute}
.serif{font-family:"Noto Serif",Georgia,serif;font-weight:700}

/* hero */
.hero{position:absolute;left:0;top:0;width:928px;height:530px;background:var(--dark);overflow:hidden}
.hero-photo{position:absolute;left:300px;top:0;width:628px;height:530px;background:radial-gradient(ellipse at 70% 40%,#8a6650 0%,#4a3a30 35%,#1f2a2a 75%)}
.hero-fade{position:absolute;left:0;top:0;width:928px;height:530px;background:linear-gradient(90deg,var(--dark) 30%,rgba(20,38,42,.6) 55%,rgba(20,38,42,0) 80%),linear-gradient(0deg,rgba(20,38,42,.7) 0%,rgba(20,38,42,0) 40%)}
.brand{position:absolute;left:78px;top:27px;color:var(--white);font-family:"Nunito Sans",Arial,sans-serif;font-weight:600;font-size:12px;line-height:14px}
.nav{position:absolute;top:28px;left:0;width:928px;font-size:10px;color:var(--white)}
.nav span{position:absolute}
.hero h1{position:absolute;left:78px;top:158px;font-size:40px;line-height:39px;color:var(--white)}
.hero p{position:absolute;left:78px;top:268px;width:470px;font-size:18.5px;line-height:23.5px;color:var(--white)}
.btn{position:absolute;height:39px;width:124px;display:flex;align-items:center;justify-content:center;font-size:10px;font-weight:600;color:var(--white);border-radius:2px}
.btn-solid{background:var(--wood)}
.btn-line{border:1px solid var(--wood)}

/* services */
.section-title{font-size:21px;color:var(--ink)}
.card{position:absolute;width:180px;height:186px;border:3px solid var(--wood);text-align:center;color:var(--ink)}
.card svg{position:absolute;left:50%;top:18px;transform:translateX(-50%)}
.card h3{position:absolute;left:6px;right:6px;top:88px;font-size:14px;font-weight:400;line-height:17px}
.card p{position:absolute;left:26px;right:26px;top:137px;font-size:9px;line-height:11px}
.card-list{background:var(--wood);color:var(--white);text-align:left}
.card-list ul{list-style:none;padding:18px 8px 0 12px}
.card-list li{font-size:8.6px;line-height:10.5px;margin-bottom:8.5px;padding-left:10px;position:relative}
.card-list li:before{content:"";position:absolute;left:0;top:3px;width:5px;height:5px;border-radius:50%;background:var(--white)}

/* project */
.project{position:absolute;left:0;top:1327px;width:928px;height:317px;background:var(--dark)}
.project h2{position:absolute;left:78px;top:60px;font-size:21px;line-height:23px;color:var(--white)}
.project p{position:absolute;left:78px;top:125px;width:290px;font-size:13.5px;line-height:17px;color:var(--white)}
.shot{position:absolute;top:21px;width:199px;height:275px}

/* about */
.about{position:absolute;left:0;top:1644px;width:928px;height:323px;background:var(--wood);overflow:hidden}
.about-photo{position:absolute;left:380px;top:0;width:548px;height:323px;background:radial-gradient(ellipse at 70% 45%,#a08468 0%,#7a5e44 40%,rgba(184,116,48,0) 80%)}
.about h2{position:absolute;left:78px;top:108px;font-size:21px;color:var(--white)}
.about p{position:absolute;left:78px;top:148px;width:440px;font-size:13.5px;line-height:17px;color:var(--white)}

/* contact */
.contact h2{position:absolute;left:78px;top:2050px;font-size:21px}
.address{position:absolute;left:78px;top:2106px;font-size:13.5px;line-height:17px}
.line{position:absolute;left:78px;font-size:13.5px;display:flex;align-items:center;gap:10px}
.map{position:absolute;left:560px;top:2013px;width:290px;height:275px;background:linear-gradient(135deg,#eef0f4,#dfe4ec)}
</style>
</head>
<body>
<div class="page">

  <header class="hero">
    <div class="hero-photo" role="img" aria-label="Nahaufnahme einer Hand, die mit einem Hobel Holz bearbeitet"></div>
    <div class="hero-fade"></div>
    <div class="brand">Tischlerei Wendholt</div>
    <nav class="nav">
      <span style="left:349px">Start</span>
      <span style="left:425px">Über uns</span>
      <span style="left:507px">Leistungen</span>
      <span style="left:591px">f.wendholt@tischlerei-wendholt.de</span>
      <span style="left:775px">(0 37 00) 4 81 56</span>
    </nav>
    <h1 class="serif">Maßarbeit aus Holz.<br>Mit Erfahrung seit 1928.</h1>
    <p>Wir planen, fertigen und montieren individuelle Tischlerarbeiten – präzise, langlebig und passend zu Ihren Anforderungen.</p>
    <a class="btn btn-solid" style="left:78px;top:376px">Kontakt aufnehmen</a>
    <a class="btn btn-line" style="left:217px;top:376px">Leistungen ansehen</a>
  </header>

  <h2 class="abs serif section-title" style="left:78px;top:608px">Was wir machen</h2>

  <div class="card" style="left:80px;top:673px">
    <svg width="80" height="40" viewBox="0 0 80 40" fill="none" stroke="#b87430" stroke-width="1.5"><rect x="2" y="4" width="34" height="30"/><line x1="10" y1="4" x2="10" y2="34"/><line x1="18" y1="4" x2="18" y2="34"/><line x1="26" y1="4" x2="26" y2="34"/><rect x="34" y="14" width="42" height="16" rx="3"/><rect x="40" y="8" width="30" height="8" rx="2"/></svg>
    <h3>Wohnraummöbel</h3><p>Maßgefertigte Möbel für Wohnräume.</p>
  </div>
  <div class="card card-list" style="left:276px;top:673px">
    <ul>
      <li>Individuelle Küchen</li>
      <li>Individuelle Badmöbel</li>
      <li>Original Ravenholz-Küchen aus Sachsen</li>
      <li>Aus Alt mach Neu - Küchenfronten- und Arbeitsplattenwechsel</li>
      <li>Arbeitsplatten aus Naturstein</li>
      <li>Nischenrückwände mit Bild / Lackierung / Digitaldruck</li>
    </ul>
  </div>
  <div class="card" style="left:472px;top:673px">
    <svg width="50" height="50" viewBox="0 0 50 50" fill="none" stroke="#b87430" stroke-width="1.5"><path d="M6 6 L44 44 M44 6 L6 44"/><rect x="2" y="2" width="8" height="8"/><path d="M40 40 l6 6"/></svg>
    <h3>Innenausbau (Wand,<br>Decke, Boden)</h3><p>Ausbau für Wand, Decke und Boden.</p>
  </div>
  <div class="card" style="left:668px;top:673px">
    <svg width="46" height="52" viewBox="0 0 46 52" fill="none" stroke="#b87430" stroke-width="1.5"><rect x="4" y="2" width="38" height="46"/><rect x="9" y="7" width="12" height="18"/><rect x="25" y="7" width="12" height="18"/><rect x="9" y="28" width="12" height="16"/><rect x="25" y="28" width="12" height="16"/><line x1="0" y1="50" x2="46" y2="50"/></svg>
    <h3>Fenster und Türen</h3><p>Passgenaue Elemente<br>aus Holz.</p>
  </div>

  <div class="card" style="left:80px;top:870px">
    <svg width="54" height="52" viewBox="0 0 54 52" fill="none" stroke="#b87430" stroke-width="1.5"><rect x="8" y="2" width="16" height="12"/><rect x="2" y="20" width="50" height="30"/><rect x="8" y="26" width="38" height="18"/><line x1="2" y1="20" x2="52" y2="20"/></svg>
    <h3>Praxiseinrichtungen /<br>Ladenbau</h3><p>Einrichtungen für Praxen und Geschäftsräume.</p>
  </div>
  <div class="card" style="left:276px;top:870px">
    <svg width="48" height="52" viewBox="0 0 48 52" fill="none" stroke="#b87430" stroke-width="1.5"><rect x="4" y="2" width="40" height="44"/><rect x="10" y="8" width="28" height="24"/><line x1="0" y1="50" x2="48" y2="50"/></svg>
    <h3>Museumsarchitektur</h3><p>Lösungen für Ausstellungen und Museen.</p>
  </div>
  <div class="card" style="left:472px;top:870px">
    <svg width="50" height="52" viewBox="0 0 50 52" fill="none" stroke="#b87430" stroke-width="1.5"><rect x="2" y="10" width="46" height="40"/><rect x="20" y="2" width="10" height="16"/><line x1="25" y1="18" x2="25" y2="30"/><line x1="8" y1="40" x2="42" y2="40"/></svg>
    <h3>CNC-<br>Kleinserien</h3><p>Präzise Fertigung kleiner Serien.</p>
  </div>
  <div class="card" style="left:668px;top:870px">
    <svg width="50" height="52" viewBox="0 0 50 52" fill="none" stroke="#b87430" stroke-width="1.5"><rect x="2" y="2" width="46" height="48"/><line x1="6" y1="30" x2="30" y2="6"/><line x1="6" y1="44" x2="42" y2="8"/><line x1="20" y1="46" x2="44" y2="22"/></svg>
    <h3>Glaserei<br>im Haus</h3><p>Glaslösungen aus eigener Bearbeitung.</p>
  </div>

  <div class="card" style="left:80px;top:1067px">
    <svg width="50" height="48" viewBox="0 0 50 48" fill="none" stroke="#b87430" stroke-width="1.5"><path d="M2 46 H48 M2 46 V38 H12 V30 H22 V22 H32 V14 H42 V2 H48 V46"/></svg>
    <h3>Treppen</h3><p>Individuelle Treppenlösungen aus Holz.</p>
  </div>
  <div class="card" style="left:276px;top:1067px">
    <svg width="46" height="52" viewBox="0 0 46 52" fill="none" stroke="#b87430" stroke-width="1.5"><path d="M12 4 Q23 -2 30 8 V26 H10 Z"/><rect x="8" y="26" width="26" height="6"/><line x1="10" y1="32" x2="8" y2="50"/><line x1="32" y1="32" x2="34" y2="50"/></svg>
    <h3>Restauration</h3><p>Erhaltung und Aufarbeitung historischer Stücke.</p>
  </div>
  <div class="card" style="left:472px;top:1067px">
    <svg width="46" height="56" viewBox="0 0 46 56" fill="none" stroke="#b87430" stroke-width="1.5"><rect x="2" y="2" width="42" height="52"/><line x1="12" y1="14" x2="12" y2="44"/><line x1="18" y1="10" x2="18" y2="44"/><line x1="23" y1="8" x2="23" y2="44"/><line x1="28" y1="10" x2="28" y2="44"/><line x1="34" y1="14" x2="34" y2="44"/></svg>
    <h3>Orgelgehäuse</h3><p>Gehäuse für Orgelbau und Klangräume.</p>
  </div>
  <div class="card" style="left:668px;top:1067px">
    <svg width="50" height="50" viewBox="0 0 50 50" fill="none" stroke="#b87430" stroke-width="1.5"><circle cx="25" cy="25" r="14"/><circle cx="25" cy="25" r="6"/><path d="M25 3v6M25 41v6M3 25h6M41 25h6M9 9l4 4M37 37l4 4M41 9l-4 4M9 41l4-4"/></svg>
    <h3>Serviceleistungen</h3><p>Reparatur, Wartung und Beratung.</p>
  </div>

  <section class="project">
    <h2 class="serif">Sie planen ein<br>individuelles Projekt?</h2>
    <p>Ob Möbel, Küche, Innenausbau oder Sonderanfertigung – wir beraten Sie persönlich und finden die passende Lösung.</p>
    <a class="btn btn-solid" style="left:76px;top:201px">Kontakt aufnehmen</a>
    <div class="shot" style="left:444px;background:linear-gradient(160deg,#7a7874,#a58a64 55%,#5a4c3e)" role="img" aria-label="Schwebende Holztreppe mit Sessel vor Betonwand"></div>
    <div class="shot" style="left:652px;background:linear-gradient(170deg,#8a6a48,#c8b08a 45%,#6a5036)" role="img" aria-label="Küche aus Holz mit rundem Esstisch und Stühlen"></div>
  </section>

  <section class="about">
    <div class="about-photo" role="img" aria-label="Tischler bei der Arbeit an einem Holzbrett"></div>
    <h2 class="serif">Wer wir sind</h2>
    <p>Seit Generationen steht die Tischlerei Wendholt für zuverlässiges Handwerk, durchdachte Planung und individuelle Lösungen aus Holz. Mit Erfahrung, Präzision und moderner Technik entstehen Projekte, die funktional überzeugen und lange Bestand haben.</p>
  </section>

  <section class="contact">
    <h2 class="serif">Wie Sie uns erreichen</h2>
    <div class="address">Tischlerei Wendholt GmbH<br>Lindenweg 12<br>09100 Eichtal</div>
    <div class="line" style="top:2179px"><svg width="13" height="13" viewBox="0 0 13 13" fill="none" stroke="#1d2a2c" stroke-width="1"><path d="M2 1h3l1 3-2 1a7 7 0 0 0 4 4l1-2 3 1v3a1 1 0 0 1-1 1A11 11 0 0 1 1 2a1 1 0 0 1 1-1z"/></svg>(0 37 00) 4 81 56</div>
    <div class="line" style="top:2205px"><svg width="13" height="13" viewBox="0 0 13 13" fill="none" stroke="#1d2a2c" stroke-width="1"><rect x="1" y="3" width="11" height="8"/><path d="M1 3l5.5 4L12 3"/></svg>f.wendholt@tischlerei-wendholt.de</div>
    <div class="line" style="top:2231px"><svg width="13" height="13" viewBox="0 0 13 13" fill="none" stroke="#1d2a2c" stroke-width="1"><path d="M6.5 12s4-4 4-7a4 4 0 0 0-8 0c0 3 4 7 4 7z"/><circle cx="6.5" cy="5" r="1.5"/></svg>Anfahrt / Karte ansehen</div>
    <div class="map" role="img" aria-label="Stadtplan mit Standort der Tischlerei"></div>
  </section>

</div>
</body>
</html>
```